PACKAGING DESIGN - HOT New Brand of Haircare

We are creating a NEW haircare brand that will need to stand out on retail shelves. This is a luxury product at an affordable price. We will look for designs for 2 different formulas - Shine Boosting Shampoo & Moisturizing Conditioner containing Argan Oil and the other will be a Nourishing Shampoo & Hydrating Conditioner containing Coconut Oil.Packaging will be 32 oz bottle with pump (either Boston Round or Bullet shape). Examples are shown on the brief. This product will be sold at national retailers and needs to look like a brand that is sold at a high end boutique or salon.
Updates

Need extra days to review

Target Market(s)

Women and Men 20s - 40s who want high end hair care

Font styles to use
Sans Serif

Colors

Designer to choose colors to be used in the design.

Requirements
Must have
• Label design for the existing bottle - 4 different SKUs. (see attached brief)

```html
<!DOCTYPE html>
<html lang="en">
<head>
<meta charset="utf-8">
<title>Shampoo Back Label</title>
<link rel="stylesheet" href="https://fonts.googleapis.com/css2?family=Oswald:wght@500;600&family=Roboto:wght@400&display=swap">
<style>
  :root {
    --label-brown: #683a14;
    --frame-green: #3dff12;
    --frame-white: #ffffff;
    --text-cream: #ffffff;
    --heading-cream: #ffffff;
    --upc-ink: #0d0d0d;
  }
  * { margin: 0; padding: 0; box-sizing: border-box; }
  html, body {
    width: 1200px;
    height: 2334px;
    overflow: hidden;
    background: var(--label-brown);
  }
  .label {
    position: relative;
    width: 1200px;
    height: 2334px;
    background: var(--label-brown);
    overflow: hidden;
  }
  .frames {
    position: absolute;
    inset: 0;
    width: 1200px;
    height: 2334px;
  }
  .brand-mark {
    position: absolute;
    left: 182px;
    top: 208px;
    width: 252px;
    height: 312px;
    border-radius: 48% 48% 50% 50% / 40% 40% 60% 60%;
    background: radial-gradient(circle at 50% 45%, #3dfa12 0%, #2fc40e 55%, #3a2a1c 100%);
  }
  .section-heading {
    position: absolute;
    font-family: "Oswald", "Arial Narrow", sans-serif;
    font-weight: 600;
    font-size: 40px;
    letter-spacing: 0.5px;
    line-height: 1;
    color: var(--heading-cream);
    text-transform: uppercase;
  }
  .section-body {
    position: absolute;
    font-family: "Roboto", Arial, sans-serif;
    font-weight: 400;
    font-size: 40px;
    line-height: 66px;
    color: var(--text-cream);
  }
  .benefits-heading { left: 476px; top: 220px; }
  .benefits-body { left: 476px; top: 276px; width: 560px; }
  .use-heading { left: 169px; top: 629px; }
  .use-body { left: 169px; top: 690px; width: 880px; }
  .ingredients-heading { left: 169px; top: 1020px; }
  .ingredients-body { left: 169px; top: 1080px; width: 900px; }
  .recycle-mark {
    position: absolute;
    left: 68px;
    top: 2023px;
    width: 231px;
    height: 270px;
    background: var(--frame-green);
    clip-path: polygon(50% 0%, 100% 82%, 0% 82%);
  }
  .upc-box {
    position: absolute;
    left: 702px;
    top: 2041px;
    width: 430px;
    height: 261px;
    background: var(--frame-white);
    display: flex;
    align-items: center;
    justify-content: center;
    font-family: "Oswald", "Arial Narrow", sans-serif;
    font-weight: 600;
    font-size: 140px;
    line-height: 1;
    color: var(--upc-ink);
  }
</style>
</head>
<body>
<main class="label">
  <svg class="frames" viewBox="0 0 1200 2334" aria-hidden="true">
    <rect x="62" y="62" width="1014" height="1864" fill="none" stroke="var(--frame-green)" stroke-width="18"/>
    <rect x="98" y="114" width="999" height="1850" fill="none" stroke="var(--frame-white)" stroke-width="12"/>
    <rect x="137" y="151" width="1006" height="1863" fill="none" stroke="var(--frame-green)" stroke-width="18"/>
  </svg>

  <div class="brand-mark" role="img" aria-label="Green heart emblem with a water droplet"></div>

  <h2 class="section-heading benefits-heading">Benefits</h2>
  <p class="section-body benefits-body">Cleanses and helps maintain an ideal moisture balance to promote healthy-looking and manageable hair.</p>

  <h2 class="section-heading use-heading">Suggested Use</h2>
  <p class="section-body use-body">Massage through wet hair and scalp. Rinse<br>thoroughly. Add more water to activate a rich<br>lather. Follow with Golden Veil Hydrating<br>Conditioner.</p>

  <h2 class="section-heading ingredients-heading">Ingredients</h2>
  <p class="section-body ingredients-body">Water / Eau (Aqua), Cetyl Alcohol,<br>Cetrimonium Chloride, Behentrimonium<br>Chloride, Isopropyl Palmitate, Glycerin,<br>Cyclopentasiolxane, Argania Spinosa Kernel<br>Oil (Argan Oil), Butryspermum Parkii (Shea)<br>Butter, Olea Europaea (Olive) Fruit Oil, Cocos<br>Nucifera (Coconut) Oil, Glycine Soja (Soybean)<br>Protein, Hydrolyzed Keratin, Hydrolyzed Corn<br>Protein, Hydrolyzed Soy Protein, Panthenol,<br>(Vitamin B5), Stearyl Alcohol, Dimethiconol,<br>Dimethicone, Phenoxyethanol, Citric Acid,<br>Fragrance (Parfum).</p>

  <div class="recycle-mark" role="img" aria-label="Green recycling symbol"></div>
  <div class="upc-box">UPC</div>
</main>
</body>
</html>
```